Wine Bottle Label for Tall Fern Cellars

We are a small, newly established winery in need of an original, bold and outstanding bottle label design for our Tall Fern wine.

Our vineyard and winery are located on a 200 acre farm in a remote part of southern Oregon. The name "Tall Fern" was inspired by the large, overgrown size of all of the foliage here, including our grapevines. Things grow large and vigorous in Oregon! And everything is very lush and green. It is almost surreal or other-worldly, like the landscapes seen in the Keeper of The Hollows movies, or the land of Yarrowmere. It is a place that makes you say "wow" with its epic, large scale, natural beauty.

The name "Tall Fern" also captures the essence of our wine. It is big in flavor, quality and color. Our first release is a Pinot Noir (red). Pinot Noir wines often are subtle in flavor and thin in their color. Our label should convey that our Pinot Noir is a much more robust, darker, heavier, meatier, more flavorful wine that is a lot more fun than an "ordinary" wine. At the same time, this wine is not cheap, and so nothing in the label should convey "bargain," "low price," or "cheapness." This is a fine wine with a sense of adventure. Be sure to convey "quality" with your design along with "big," "adventure" and "fun".

The label should appeal to a younger demographic, both male and female, between the ages of 21 and 35. It should be non-traditional and adventurous and suggest a pushing of boundaries and a breaking of rules. This Pinot Noir does not conform to the normal "limitations" of the variety, therefore the label should not conform. It should have an "organic" or "natural" or "agricultural" vibe, as opposed to something mechanical or technical. It should, however, be contemporary. Do not confuse "natural" or "organic" with being nostalgic or old school. Think "agri-hipsters."

The label should be designed to fit on a Burgundy-style wine bottle (photo attached for reference). (Note: All Pinot Noir and Chardonnay is bottled in Burgundy bottles, If you are not sure about the bottle shape you can go to a local store and compare the various bottles. Locate a bottle of Pinot Noir or Chardonnay or anything identified as a "Burgundy Wine," and it should be the correct bottle. The tall, skinny bottles used for Cabernet Sauvignon are NOT correct)). Please see the "Must Have" notes for more on the bottle.

In summary, the final project should be a wine bottle label design that conveys bigness, vastness, adventurous, non-traditional, high quality wine. A good tagline to keep in mind is "Living Large."

Target Market(s)

Young, hip, non-conformist wine drinkers aged 21-35 with a sense of adventure and an appreciation of quality.

Industry/Entity Type

School

Requirements
Must have
• *Must contain the words:

Tall Fern (the brand)
2013 Pinot Noir (the vintage year and variety)

*The label must be designed to fit a Burgundy-style wine bottle. A photo is attached for reference.

*Additionally, the label needs to fit on the lower, widest part of the bottle. The label will be printed on sticky paper and rolled onto the bottle with a machine. The machine cannot apply labels to the neck of the bottle. The maximum size of a label that will fit this space is 5.5 inches wide by 4.5 inches tall. You DO NOT have to fill ALL of this space or confine the label shape to a rectangle, but the label cannot exceed this size or it won't stick to the bottle properly. It will really help if you can put your hands on an actual bottle to see the logistics of applying the label. But if that is not possible, just do your best with the instructions you have. I am confident the winning design could be adjusted to fit the bottle, if necessary
Nice to have
• *Wine grape leaf or leaves.

*A concept I have been playing with is sunlight shining through leaves like light through a Kessler lamp or a stained glass window. This is NOT a requirement for this label. However, if the concept inspires and idea, I would be most happy to see it.
Should not have
• IF a leaf or leaves are included in the design (not a requirement) they MUST be wine grapevine leafs and preferably leaves of the Pinot Noir vine. Do not use generic leaves or identifiable leaves such as oak leaves, maple leaves, or anything that looks like the Canadian flag or the Dunmore Ice Hawks hockey logo. Reference the attached photos of wine grape leaves to see the correct leaf type. I am happy to email more photos upon request. These photos may be used in whole or in part in your design, however, a leaf from a photo is NOT a requirement, nor is the image of a leaf or leaves.

This label should NOT be designed for Bordeaux-style wine bottles (the tall, skinny ones).

```html
<!DOCTYPE html>
<html lang="en">
<head>
<meta charset="utf-8">
<title>Tall Fern Cellars — Pinot Noir 2013 Label</title>
<link rel="stylesheet" href="https://fonts.googleapis.com/css2?family=Roboto+Condensed:wght@400;500;700&display=swap">
<style>
  :root {
    --backdrop: #e9e6e1;
    --label-paper: #f3f3f2;
    --label-paper-edge: #e4e4e3;
    --ink-dark: #4a3f43;
    --ink-soft: #6e6568;
    --accent-tan: #c9a06c;
    --vintage-box: #a9a6a7;
    --vintage-figure: #e4e2e3;
    --leaf-light: #8fb46a;
    --leaf-mid: #5f8f3e;
    --leaf-deep: #2f5a24;
  }
  * { margin: 0; padding: 0; box-sizing: border-box; }
  html, body {
    width: 1200px;
    height: 900px;
    overflow: hidden;
    background: var(--backdrop);
  }
  .canvas {
    position: relative;
    width: 1200px;
    height: 900px;
  }
  .label {
    position: absolute;
    left: 280px;
    top: 90px;
    width: 640px;
    height: 720px;
    overflow: hidden;
    background: linear-gradient(90deg, var(--label-paper-edge) 0%, var(--label-paper) 14%, var(--label-paper) 86%, var(--label-paper-edge) 100%);
    font-family: "Roboto Condensed", "Arial Narrow", sans-serif;
  }
  .leaf-photo {
    position: absolute;
    left: 9px;
    top: 0;
    width: 582px;
    height: 490px;
    border-radius: 8% 10% 48% 40% / 6% 8% 58% 52%;
    background: radial-gradient(ellipse at 42% 30%, var(--leaf-light) 0%, var(--leaf-mid) 45%, var(--leaf-deep) 100%);
  }
  .label-footer {
    position: absolute;
    left: 16px;
    right: 0;
    top: 560px;
    display: flex;
    align-items: center;
  }
  .bottle-details {
    flex: none;
    width: 64px;
    color: var(--ink-soft);
    font-size: 14px;
    font-weight: 700;
    line-height: 1.35;
    letter-spacing: 0.5px;
  }
  .bottle-details .rule {
    width: 40px;
    height: 2px;
    margin: 6px 0;
    background: var(--accent-tan);
  }
  .title-block {
    flex: none;
    margin-left: 22px;
    color: var(--ink-dark);
  }
  .brand-name {
    font-size: 72px;
    font-weight: 700;
    line-height: 1;
    letter-spacing: -0.5px;
    white-space: nowrap;
  }
  .variety-row {
    display: flex;
    align-items: flex-end;
    justify-content: space-between;
    margin-top: 8px;
  }
  .variety {
    font-size: 40px;
    font-weight: 500;
    line-height: 1;
    word-spacing: 6px;
    white-space: nowrap;
  }
  .accent-mark {
    flex: none;
    width: 30px;
    height: 30px;
    margin-left: 16px;
    margin-bottom: 2px;
  }
  .vintage {
    flex: none;
    margin-left: auto;
    padding: 20px 12px;
    background: var(--vintage-box);
  }
  .vintage-year {
    display: block;
    color: var(--vintage-figure);
    font-size: 80px;
    font-weight: 700;
    line-height: 1;
    letter-spacing: -1px;
  }
</style>
</head>
<body>
  <main class="canvas">
    <section class="label" aria-label="Tall Fern Pinot Noir 2013 wine label">
      <div class="leaf-photo" role="img" aria-label="Photograph of a large green Pinot Noir grapevine leaf hanging from the top of the label"></div>

      <div class="label-footer">
        <div class="bottle-details">
          <p>13.5%</p>
          <p>750 ml</p>
          <div class="rule"></div>
          <p>OREGON</p>
        </div>

        <div class="title-block">
          <h1 class="brand-name">TALL FERN</h1>
          <div class="variety-row">
            <p class="variety">PINOT NOIR</p>
            <svg class="accent-mark" viewBox="0 0 30 30" aria-hidden="true">
              <polygon points="30,0 30,30 0,30" fill="var(--accent-tan)"/>
            </svg>
          </div>
        </div>

        <div class="vintage">
          <span class="vintage-year">2013</span>
        </div>
      </div>
    </section>
  </main>
</body>
</html>
```